New online business - used mobile phones - needs unique eye catching web design that sets it apart

The Handset Bazaar
We are a new business looking for a rapid response for our web site design. We don't want a normal website....... we need to be creative - most important PLEASE view the attached files uploaded 3 March to ensure you get us :)
.
The Handset Bazaar buys new and damaged mobile phones from the public. A simple process they complete to sell their mobile to us; we want our website to reflect this.
Our website needs to be modern, edgy and fun, not corporate and definitely not like any other mobile phone buying site in the world today!!
Our name was taken from a play on the share/stock market which we have tried to bring into the design ....... it hasn't worked with early designs submitted. Now taking a different approach. Refer to new attached files which should help you visualise our concept.

We like layout from Artisan Hive – plvendrake #7318290 design as this is very close to our layout vision.
The first page to tell the public what we do, how we do it, and then they click to accept the instant online quote. (page two they complete details about the mobiles model & condition they are selling, then page three complete their personal details).
Our background preference is dark, blackboard or dark with slight texture
a) We love white on black/dark background either typewriter font or look like hand drawn refer to attached files & quillandfennel.com.au site to see. Would Label font work???

b) Where the light blue colour is on #7318290 this needs to be like chromadex colour classic green, fern green or bright green, not fluorescent lime green or an insipid green.

c) The banner says The Handset Bazaar is open........... for buying mobiles for cash $$$ (we need people to know we BUY used/damaged phones)

d) We love colour either solid colour or looks like it has been coloured in on our dark background. Open to white or pastel background versions refer to attached coffee file.
We like Chromadex Orange 021,Haute Red,Dazzling Blue, Cyan Blue, Beetroot Purple, Island Green.
e) How it works – underneath this title put Our deal …………. It’s easy as…………..quote, post, get paid!!!
Quote – first circle hand drawn icon showing mobile phone & $ sign. Underneath it says .....Obtain Quote for Model & Condition
Post – second circle hand drawn icon show parcel. Underneath it says Free Post
Paid – third circle hand drawn icon showing large $ sign. Underneath it says Payment in Two Days
Plans - is swapped for wording- Get Market Quote with a large button which says GO or CLICK HERE (they click on the button & it takes them to the next page)
f) FAQ
Allow for six FAQ’s we will forward correct content to you for final design layout.

g) About Us
Please allow about a paragraph of text here, we will forward correct content to you for final design layout.
h) Contact Us
At the bottom where normal website have ………. home, contact details, blog, etc, please only put Email us & Call us, then social media icons for FB, Linked In and Chirper

I) LOGO We don’t have one yet, just put The Handset Bazaar at the top & it needs to be large sized font ................we are new and we need to push our name
If you are not clear on our vision ..........please email me and I will reply very quickly.
Thank you for taking the time to read & understand & get us:)

Target Market(s)

20-45 years any body with a spare smart phone that is lying around and they can get cash for. Target market could be slightly older to 50 but focus of 20-40's

Industry/Entity Type

Business

Number of Pages Required

3 page

Font styles to use
Other font styles liked:
• handwritten font or typewriter font

Requirements
Must have
• Read only attached files dated 4 March, tech error with other files, being removed.
• 1 Layout design of Artisan Hive – plvendrake #7318290
• 2 Hand drawn icons - refer to files
• 3 White font needs to look like hand written refer to quillandfennel.com.au or typewriter font - large size font
• 4 Main colours are Black or dark background, green with white text, preference is hand drawn font. The three circles for quote, post & pay with hand drawn icons can be any colour ...... Purple for quote, orange for post & green for paid
• 5 Big green button underneath 3 circles quote/post/pay - customers click on big button to get instant quote
Nice to have
• Coloured in hand drawings as per file
• Great Hand drawings coloured in
Should not have
• NO template designs so it look like you just put some text & a photo. Don't fill the page with mobile phones, one or two is ok, mobile phone pictures date so fast.
• Cartoons

```html
<!DOCTYPE html>
<html lang="en">
<head>
<meta charset="utf-8">
<title>The Handset Bazaar</title>
<link rel="stylesheet" href="https://fonts.googleapis.com/css2?family=Cabin+Sketch:wght@400;700&family=Kalam:wght@300;400&family=Fredoka:wght@600&family=Open+Sans:wght@400;600&display=swap">
<style>
  :root {
    --night-top: #123f63;
    --night-mid: #0c2b4b;
    --night-low: #0a1d35;
    --chalk: #eef1f2;
    --chalk-soft: #d3d9de;
    --fern: #b5cea6;
    --fern-dark: #8fb07f;
    --quote-purple: #c59ec0;
    --quote-ink: #b98ab0;
    --post-orange: #e0a477;
    --post-ink: #d9915a;
    --paid-teal: #7fb3c0;
    --paid-ink: #6fa4b0;
    --frame-ink: #4a4f57;
    --footer: #070809;
  }
  * { box-sizing: border-box; margin: 0; padding: 0; }
  html, body { width: 1200px; height: 2311px; overflow: hidden; }
  body {
    position: relative;
    background:
      repeating-linear-gradient(90deg, rgba(255,255,255,.015) 0 2px, transparent 2px 7px),
      linear-gradient(180deg, var(--night-top) 0%, #11486e 18%, var(--night-mid) 40%, var(--night-low) 70%, #0b1b30 100%);
    color: var(--chalk);
    font-family: "Kalam", cursive;
  }
  .abs { position: absolute; }
  .sketch { font-family: "Cabin Sketch", cursive; font-weight: 700; }

  .site-title { top: 38px; left: 0; width: 1200px; text-align: center; font-size: 104px; line-height: 1; color: var(--chalk); letter-spacing: 2px; }

  .hero { left: 77px; top: 183px; width: 1080px; height: 645px; }
  .hero-frame { position: absolute; inset: 0; }
  .hero-screen { position: absolute; left: 58px; top: 50px; width: 960px; height: 540px; }
  .hero-phone { position: absolute; left: 29px; top: 44px; width: 385px; height: 591px; border-radius: 30px;
    background: linear-gradient(160deg, #6c6f74 0%, #2a2c30 10%, #1a4f7a 30%, #3d8bb8 55%, #2b2d31 88%, #7a7c80 100%); }
  .hero-headline { position: absolute; left: 420px; top: 155px; width: 640px; text-align: center; font-family: "Fredoka", sans-serif; font-weight: 600; font-size: 66px; line-height: 1; color: #fff; }
  .hero-tagline { position: absolute; left: 420px; top: 300px; width: 640px; text-align: center; font-family: "Kalam", cursive; font-size: 62px; line-height: 62px; color: #fff; }

  .deal-line { top: 868px; left: 0; width: 1200px; text-align: center; font-size: 46px; color: var(--chalk-soft); }

  .step { top: 935px; width: 360px; text-align: center; }
  .step-1 { left: 27px; }
  .step-2 { left: 408px; }
  .step-3 { left: 793px; }
  .step-tile { position: relative; width: 250px; height: 270px; margin: 0 auto; }
  .step-tile svg { position: absolute; inset: 0; }
  .step-art { position: absolute; left: 28px; top: 28px; width: 194px; height: 214px; }
  .step-1 .step-art { background: var(--quote-purple); }
  .step-2 .step-art { background: var(--post-orange); }
  .step-3 .step-art { background: var(--paid-teal); }
  .step-name { font-size: 54px; line-height: 1; margin-top: 12px; }
  .step-1 .step-name { color: var(--quote-ink); }
  .step-2 .step-name { color: var(--post-ink); }
  .step-3 .step-name { color: var(--paid-ink); }
  .step-note { font-size: 36px; line-height: 34px; color: var(--chalk); margin-top: 6px; }

  .quote-call { top: 1383px; left: 0; width: 1200px; text-align: center; font-size: 50px; color: var(--chalk-soft); }
  .go-button { left: 400px; top: 1464px; width: 395px; height: 232px; }
  .go-label { position: absolute; left: 0; top: 20px; width: 380px; text-align: center; font-family: "Cabin Sketch", cursive; font-weight: 700; font-size: 118px; color: #eef3ea; }

  .info-heading { top: 1735px; font-size: 52px; color: var(--chalk-soft); }
  .about-heading { left: 67px; }
  .faq-heading { right: 64px; }
  .about-text { left: 67px; top: 1808px; width: 525px; font-size: 19px; line-height: 24px; text-align: justify; color: var(--chalk); font-weight: 300; }
  .faq-list { left: 651px; top: 1805px; width: 485px; list-style: none; font-family: "Open Sans", sans-serif; font-size: 14.5px; line-height: 21px; color: var(--chalk); }
  .faq-list li + li { margin-top: 21px; }
  .more-link { font-family: "Open Sans", sans-serif; font-size: 18px; font-weight: 600; color: #fff; text-decoration: none; }
  .about-more { left: 510px; top: 1966px; }
  .faq-more { left: 1062px; top: 1958px; }

  .social { top: 2026px; left: 0; width: 1200px; display: flex; justify-content: center; gap: 18px; font-family: "Open Sans", sans-serif; font-size: 13px; color: var(--chalk-soft); }
  .social span { display: inline-flex; align-items: center; gap: 5px; }
  .social i { display: inline-block; width: 18px; height: 18px; background: #3a78b5; border-radius: 3px; }

  .site-footer { left: 0; top: 2067px; width: 1200px; height: 244px; background: var(--footer); text-align: center; }
  .footer-title { padding-top: 36px; font-size: 66px; line-height: 1; color: var(--chalk); }
  .footer-contact { margin-top: 20px; font-size: 34px; line-height: 38px; color: #fff; }
</style>
</head>
<body>
  <h1 class="abs site-title sketch">The Handset Bazaar</h1>

  <section class="abs hero">
    <svg class="hero-frame" viewBox="0 0 1080 645" width="1080" height="645">
      <path d="M20 18 C 260 2, 520 30, 780 12 S 1060 8, 1066 30 C 1074 220, 1052 420, 1070 622 C 820 640, 560 618, 300 636 S 30 640, 14 626 C 4 420, 26 220, 20 18 Z" fill="var(--fern)"/>
      <defs>
        <linearGradient id="screenGlow" x1="0" y1="0" x2="1" y2="1">
          <stop offset="0" stop-color="#1f8fae"/>
          <stop offset=".5" stop-color="#1ab0c4"/>
          <stop offset="1" stop-color="#0f6d8c"/>
        </linearGradient>
      </defs>
      <path d="M58 56 C 300 44, 640 66, 1020 50 C 1030 220, 1012 420, 1022 590 C 760 602, 400 580, 58 596 C 50 420, 66 220, 58 56 Z" fill="url(#screenGlow)" role="img" aria-label="Glowing teal digital circuitry backdrop"/>
    </svg>
    <div class="hero-phone" role="img" aria-label="Photo of a black touchscreen smartphone"></div>
    <p class="hero-headline">The<br>Handset Bazaar</p>
    <p class="hero-tagline">is open for<br>buying mobiles<br>for cash $$$</p>
  </section>

  <p class="abs deal-line sketch">Our deal ...It’s easy as...quote, post, get paid !!</p>

  <div class="abs step step-1">
    <div class="step-tile">
      <div class="step-art" role="img" aria-label="Hand drawn mobile phone on purple"></div>
      <svg viewBox="0 0 250 270"><path d="M14 16 L236 10 L240 256 L10 260 Z M30 30 L222 26 L224 242 L28 246 Z" fill="none" stroke="var(--frame-ink)" stroke-width="9" stroke-linejoin="round"/></svg>
    </div>
    <p class="step-name sketch">Quote</p>
    <p class="step-note">Obtain quote for<br>model &amp; condi-<br>tion</p>
  </div>

  <div class="abs step step-2">
    <div class="step-tile">
      <div class="step-art" role="img" aria-label="Hand drawn parcel box on orange"></div>
      <svg viewBox="0 0 250 270"><path d="M14 16 L236 10 L240 256 L10 260 Z M30 30 L222 26 L224 242 L28 246 Z" fill="none" stroke="var(--frame-ink)" stroke-width="9" stroke-linejoin="round"/></svg>
    </div>
    <p class="step-name sketch">Post</p>
    <p class="step-note">Free post</p>
  </div>

  <div class="abs step step-3">
    <div class="step-tile">
      <div class="step-art" role="img" aria-label="Hand drawn money bag with dollar sign on teal"></div>
      <svg viewBox="0 0 250 270"><path d="M14 16 L236 10 L240 256 L10 260 Z M30 30 L222 26 L224 242 L28 246 Z" fill="none" stroke="var(--frame-ink)" stroke-width="9" stroke-linejoin="round"/></svg>
    </div>
    <p class="step-name sketch">Get Paid</p>
    <p class="step-note">Payment into<br>your bank ac-<br>count within<br>two days</p>
  </div>

  <p class="abs quote-call sketch">Get Market Quote</p>

  <a class="abs go-button" href="#quote" aria-label="Go to market quote">
    <svg viewBox="0 0 395 232" width="395" height="232">
      <path d="M12 150 L372 166 L388 204 L40 226 L14 196 Z" fill="#f4f4f4" stroke="#1b2430" stroke-width="5"/>
      <g stroke="#1b2430" stroke-width="5">
        <line x1="60" y1="160" x2="70" y2="222"/><line x1="95" y1="160" x2="105" y2="220"/>
        <line x1="130" y1="161" x2="140" y2="218"/><line x1="165" y1="162" x2="175" y2="216"/>
        <line x1="200" y1="163" x2="210" y2="214"/><line x1="235" y1="163" x2="245" y2="212"/>
        <line x1="270" y1="164" x2="280" y2="210"/><line x1="305" y1="164" x2="315" y2="208"/>
        <line x1="340" y1="165" x2="350" y2="206"/>
      </g>
      <path d="M8 12 L366 4 L374 170 L14 156 Z" fill="var(--fern)" stroke="#e7efe2" stroke-width="4"/>
    </svg>
    <span class="go-label">GO</span>
  </a>

  <h2 class="abs info-heading about-heading sketch">About Us</h2>
  <h2 class="abs info-heading faq-heading sketch">FAQ</h2>

  <p class="abs about-text">Lorem ipsum dolor sit amet, consectetuer adipiscing elit, sed diam nonummy nibh euismod tincidunt ut laoreet dolore magna aliquam erat volutpat. Ut wisi enim ad minim veniam, quis nostrud exerci tation ullamcorper suscipit lobortis nisl ut aliquip ex ea commodo consequat.</p>
  <a class="abs more-link about-more" href="#about">MORE&gt;</a>

  <ol class="abs faq-list">
    <li>1. Lorem ipsum dolor sit amet, consectetuer adipiscing elit, sed diam nonummy ?</li>
    <li>2. Lorem ipsum dolor sit amet, consectetuer adipiscing elit, sed diam nonummy ?</li>
  </ol>
  <a class="abs more-link faq-more" href="#faq">MORE&gt;</a>

  <nav class="abs social" aria-label="Social media">
    <span><i></i>Linkfolk</span>
    <span><i></i>Facepage</span>
    <span><i></i>Chirper</span>
  </nav>

  <footer class="abs site-footer">
    <p class="footer-title sketch">The Handset Bazaar</p>
    <p class="footer-contact">Email us at info@handsetbazaar-mail.com<br>or call us at &nbsp;0000-56782 5678</p>
  </footer>
</body>
</html>
```